Business Card Design

building company specialistloft conversion,extension ,bathrooms ,kitchens ,painting and decorating all general building work

Industry/Entity Type

Building

Contact Information for Business Card

K&R Home renewal Ltd
tel -07912468305
email-Rmarek07@brickmail.example
web in progres

Font styles to use
Sans Serif

Requirements
Must have
• name of the company
• all contact details
Nice to have
• some of the skills

```html
<!DOCTYPE html>
<html lang="en">
<head>
<meta charset="utf-8">
<title>K&amp;R Home renewal Ltd — Business Cards</title>
<link rel="stylesheet" href="https://fonts.googleapis.com/css2?family=Jost:wght@400;500&display=swap">
<style>
  :root {
    --ink: #0d0d0d;
    --paper: #f7f7f5;
    --backdrop: #d9d9d9;
    --line-soft: #8a8a8a;
  }
  * { margin: 0; padding: 0; box-sizing: border-box; }
  html, body {
    width: 1200px; height: 1000px; overflow: hidden;
    background: var(--backdrop);
    font-family: "Jost", "Futura", sans-serif;
  }
  .sheet {
    position: relative; width: 1200px; height: 1000px;
    display: flex; align-items: center; justify-content: center; gap: 40px;
  }
  .card {
    position: relative; width: 500px; height: 286px;
    box-shadow: 0 6px 18px rgba(0,0,0,0.18);
    overflow: hidden;
  }

  /* Front: black card */
  .card-front {
    background: var(--ink); color: var(--paper);
    display: flex; flex-direction: column; align-items: center; justify-content: center;
    gap: 22px;
  }
  .brand-circle {
    width: 62px; height: 62px; border-radius: 50%;
  }
  .card-front .brand-circle { background: var(--paper); }
  .brand-name {
    font-weight: 400; font-size: 17px; letter-spacing: 0.32em;
    text-transform: uppercase; white-space: nowrap;
  }

  /* Back: white card with contact band */
  .card-back { background: var(--paper); color: var(--ink); }
  .back-brand {
    position: absolute; left: 0; right: 0; top: 38px;
    display: flex; flex-direction: column; align-items: center; gap: 16px;
  }
  .card-back .brand-circle { width: 50px; height: 50px; background: var(--ink); }
  .card-back .brand-name { font-size: 14px; letter-spacing: 0.3em; }

  .rule-thin {
    position: absolute; left: 0; right: 0; height: 3px; background: var(--ink);
  }
  .rule-top { bottom: 100px; }
  .rule-bottom { bottom: 6px; }
  .contact-band {
    position: absolute; left: 0; right: 0; bottom: 16px; height: 76px;
    background: var(--ink); color: var(--paper);
    display: flex; align-items: center; padding-left: 40px; gap: 26px;
  }
  .band-divider { width: 1px; height: 40px; background: var(--line-soft); }
  .contact-list { list-style: none; display: flex; flex-direction: column; gap: 7px; }
  .contact-item {
    display: flex; align-items: center; gap: 10px;
    font-size: 13px; letter-spacing: 0.04em;
  }
  .contact-icon { width: 16px; height: 12px; flex: none; }
</style>
</head>
<body>
<main class="sheet">

  <section class="card card-front" aria-label="Business card front">
    <span class="brand-circle"></span>
    <p class="brand-name">K&amp;R Home renewal Ltd</p>
  </section>

  <section class="card card-back" aria-label="Business card back">
    <div class="back-brand">
      <span class="brand-circle"></span>
      <p class="brand-name">K&amp;R Home renewal Ltd</p>
    </div>
    <div class="rule-thin rule-top"></div>
    <div class="contact-band">
      <span class="band-divider"></span>
      <ul class="contact-list">
        <li class="contact-item">
          <svg class="contact-icon" viewBox="0 0 16 12" aria-hidden="true">
            <path d="M1 4 Q8 -1 15 4 L13 6 L11 4.5 L5 4.5 L3 6 Z" fill="#f7f7f5"/>
            <rect x="3" y="6" width="10" height="6" rx="1" fill="#f7f7f5"/>
            <circle cx="8" cy="9" r="1.6" fill="#0d0d0d"/>
          </svg>
          <span>07912468305</span>
        </li>
        <li class="contact-item">
          <svg class="contact-icon" viewBox="0 0 16 12" aria-hidden="true">
            <rect x="0.75" y="0.75" width="14.5" height="10.5" fill="none" stroke="#f7f7f5" stroke-width="1.5"/>
            <path d="M1 1 L8 7 L15 1" fill="none" stroke="#f7f7f5" stroke-width="1.5"/>
          </svg>
          <span>Rmarek07@brickmail.example</span>
        </li>
      </ul>
    </div>
    <div class="rule-thin rule-bottom"></div>
  </section>

</main>
</body>
</html>
```